Wedding Decor and Entertianment business card

Company - We run a weddings and events company called Amber Finch, we provide most entertainment and decor services to our customers.

Initial idea is ....
A simple business card with logo on the front, this will be spot varnish. On a matt black background.
The reverse will be simple contact information.

But happy to try things outside of the box and would welcome some crazy ideas.

Target Market(s)

wedding couples - 21 - 40
High end wedding venues.

Industry/Entity Type

Wedding

Contact Information for Business Card

01492 718 263
amberfinchevents.co.uk
rowan@amberfinchevents.co.uk
or
helena@amberfinchevents.co.uk

Requirements
Nice to have
• black matt background with spot varnish logo on the front.

```html
<!DOCTYPE html>
<html lang="en">
<head>
<meta charset="utf-8">
<title>Amber Finch — Business Card</title>
<link href="https://fonts.googleapis.com/css2?family=Jost:wght@400&family=Open+Sans:wght@400;700&display=swap" rel="stylesheet">
<style>
  :root {
    --page-bg: #ececee;
    --plum: #7b4f73;
    --plum-dark: #6e4467;
    --plum-soft: #8a6083;
    --lavender: #9a7a95;
    --cream: #fbfaf0;
    --ink: #2d2d2f;
    --mark-faint: #e6e4da;
    --front-text: #ecebee;
  }
  * { box-sizing: border-box; margin: 0; padding: 0; }
  html, body { width: 1200px; height: 1200px; overflow: hidden; }
  body {
    background: var(--page-bg);
    font-family: "Open Sans", Arial, sans-serif;
    position: relative;
  }
  .card {
    position: absolute;
    left: 220px;
    width: 760px;
    height: 434px;
    overflow: hidden;
  }
  .card--front { top: 140px; background: var(--plum); }
  .card--back { top: 626px; background: var(--cream); }

  .front-pattern {
    position: absolute; inset: 0;
    background: linear-gradient(135deg, var(--plum-soft) 0%, var(--plum) 50%, var(--plum-dark) 100%);
  }
  .front-lockup {
    position: absolute;
    left: 120px; top: 190px;
    display: flex; align-items: center; gap: 26px;
  }
  .front-lockup .dot {
    width: 44px; height: 44px; border-radius: 50%;
    background: var(--front-text);
  }
  .front-lockup .wordmark {
    font-family: "Jost", sans-serif;
    font-weight: 400;
    font-size: 46px;
    letter-spacing: 0.42em;
    color: var(--front-text);
    text-transform: uppercase;
  }

  .back-motif {
    position: absolute;
    left: 330px; top: -40px;
    width: 400px; height: 240px;
    border-radius: 120px;
    background: linear-gradient(90deg, var(--mark-faint), #eeece3);
    opacity: 0.9;
  }
  .back-rule {
    position: absolute;
    left: 200px; top: 268px;
    width: 320px; height: 3px;
    background: var(--lavender);
  }
  .back-rule--drop {
    left: 200px; top: 268px;
    width: 3px; height: 166px;
  }
  .back-lockup {
    position: absolute;
    left: 530px; top: 245px;
    display: flex; align-items: center; gap: 14px;
  }
  .back-lockup .dot {
    width: 34px; height: 34px; border-radius: 50%;
    background: var(--ink);
  }
  .back-lockup .wordmark {
    font-family: "Jost", sans-serif;
    font-weight: 400;
    font-size: 24px;
    letter-spacing: 0.32em;
    color: var(--lavender);
    text-transform: uppercase;
  }
  .contact {
    position: absolute;
    left: 54px; top: 96px;
  }
  .contact__name {
    font-weight: 700;
    font-size: 22px;
    color: var(--plum);
    text-transform: uppercase;
    letter-spacing: -0.01em;
    margin-bottom: 10px;
    padding-left: 34px;
  }
  .contact__list { list-style: none; }
  .contact__item {
    display: flex; align-items: center; gap: 12px;
    font-size: 15px;
    color: var(--ink);
    line-height: 24px;
  }
  .contact__icon { width: 18px; height: 18px; flex: none; }
</style>
</head>
<body>

<section class="card card--front" aria-label="Card front">
  <div class="front-pattern" role="img" aria-label="Tonal plum background with a repeating faint monogram pattern"></div>
  <div class="front-lockup">
    <span class="dot"></span>
    <span class="wordmark">Amber Finch</span>
  </div>
</section>

<section class="card card--back" aria-label="Card back">
  <div class="back-motif" role="img" aria-label="Large faint brand monogram decoration"></div>

  <div class="contact">
    <p class="contact__name">Helena Marsh</p>
    <ul class="contact__list">
      <li class="contact__item">
        <svg class="contact__icon" viewBox="0 0 24 24" aria-hidden="true"><path fill="var(--lavender)" d="M6.6 10.8a15 15 0 0 0 6.6 6.6l2.2-2.2c.3-.3.7-.4 1-.2 1.1.4 2.3.6 3.6.6.6 0 1 .4 1 1V20c0 .6-.4 1-1 1A17 17 0 0 1 3 4c0-.6.4-1 1-1h3.5c.6 0 1 .4 1 1 0 1.3.2 2.5.6 3.6.1.3 0 .7-.2 1z"/></svg>
        01492 718 263
      </li>
      <li class="contact__item">
        <svg class="contact__icon" viewBox="0 0 24 24" aria-hidden="true"><rect x="2" y="5" width="20" height="14" rx="2" fill="var(--lavender)"/><path d="M3 6l9 7 9-7" fill="none" stroke="var(--cream)" stroke-width="1.6"/></svg>
        helena@amberfinchevents.co.uk
      </li>
      <li class="contact__item">
        <svg class="contact__icon" viewBox="0 0 24 24" aria-hidden="true"><rect x="2" y="5" width="20" height="14" rx="2" fill="var(--lavender)"/><path d="M3 6l9 7 9-7" fill="none" stroke="var(--cream)" stroke-width="1.6"/></svg>
        rowan@amberfinchevents.co.uk
      </li>
      <li class="contact__item">
        <svg class="contact__icon" viewBox="0 0 24 24" aria-hidden="true"><circle cx="12" cy="12" r="10" fill="var(--lavender)"/><path d="M2 12h20M12 2c3 3 3 17 0 20M12 2c-3 3-3 17 0 20" fill="none" stroke="var(--cream)" stroke-width="1.2"/></svg>
        amberfinchevents.co.uk
      </li>
    </ul>
  </div>

  <div class="back-rule"></div>
  <div class="back-rule back-rule--drop"></div>

  <div class="back-lockup">
    <span class="dot"></span>
    <span class="wordmark">Amber Finch</span>
  </div>
</section>

</body>
</html>
```